New website for selling opensource software business to business

Website K7 Software

The open source software industry has grown enormously in recent years. More and more customers from software companies choose an open source solution. K7 Software is going to fulfill this increasing demand.

Core business

Reselling software subcriptions (business to business).

Side business

Selling consultancy and Training to customers

Goals:

- Binding of customers to K7 IT Group
- Sales of subscriptions to customer
- Enlarge network K7 IT Group
- USP: Sales of complete package, Software, consultancy and training

Products

There are a couple of products/ services that K7 will provide. Below you will find an overview of the Products:

- Bluefox subscriptions
- Crater subscriptions
- Velmor products
- Customized consultancy for the customer
- Customized training for the customer

Style

Behind the website should be a cms system like pagecraft.

Target Market(s)

Business - Business

Industry/Entity Type

Business

Coding

Coded - Design and coding required

Number of Pages Required

5+ page

Font styles to use
Other font styles liked:
• Calibri

Colors
0355a3
3176b5
85abd2

Requirements
Must have
• Home page with large photo background, About us, contact page with safe option to request more info
• Portfolio pages:
• 4 pages with a product group each:
• 1. Blue fox
• 2. Craters
• 3. Velmor
• 4. Ourtrustwall
• 1. Blue Fox
• On top space for short info/bullets about Blue fox. Further, a grid with 8 columns. In the columns 2 buttons both lead to a popup. A popup for information and a popup for requesting a quote.
• 2. Crater:
• On top space for short info/bullets about Crater. Further, a grid with 3 columns. In the columns 2 buttons both lead to a popup. A popup for information and a popup for requesting a quote.
• 1. Velmor:
• On top space for short info/bullets about Velmor. Further, a grid with 4 columns. In the columns 2 buttons both lead to a popup. A popup for information and a popup for requesting a quote.
• 2. Ourtrustwall:
• On top space for short info/bullets about Ourtrustwall. Further, a grid with 2 columns. In the columns 2 buttons both lead to a popup. A popup for information and a popup for requesting a quote.

```html
<!DOCTYPE html>
<html lang="en">
<head>
<meta charset="utf-8">
<title>K7 Software</title>
<link rel="stylesheet" href="https://fonts.googleapis.com/css2?family=Montserrat:wght@400;500;600&family=Lato:wght@400;700&display=swap">
<style>
:root{
  --indigo:#2f3193;
  --indigo-dark:#262879;
  --ink:#333;
  --muted:#555;
  --dark:#1d1d1f;
  --footer:#1f2327;
  --light:#efefef;
  --white:#fff;
  --ring:#1e6fb3;
}
*{box-sizing:border-box;margin:0;padding:0}
html,body{width:1200px;height:3913px;overflow:hidden}
body{position:relative;font-family:"Lato",sans-serif;color:var(--ink);background:var(--white)}
.abs{position:absolute}
.heading{font-family:"Montserrat",sans-serif;font-weight:500;color:var(--indigo);letter-spacing:1px}
.btn{position:absolute;display:flex;align-items:center;justify-content:center;font-family:"Lato",sans-serif;font-size:20px;text-transform:uppercase}
.btn-solid{background:var(--indigo);color:var(--white)}
.btn-white{background:var(--white);color:var(--indigo)}

/* header */
.site-header{position:absolute;left:0;top:0;width:1200px;height:125px;border-top:5px solid var(--indigo);background:var(--white)}
.brand{position:absolute;left:78px;top:18px;width:94px;height:94px;border-radius:50%;background:#f1f1f4;border:2px solid #d8d8e2;display:flex;align-items:center;justify-content:center;font-family:"Lato",sans-serif;font-weight:700;font-size:26px;color:var(--indigo)}
.nav-item{position:absolute;top:37px;height:60px;display:flex;align-items:center;font-size:19px;color:var(--muted)}
.nav-active{left:397px;width:104px;justify-content:center;background:var(--indigo);color:var(--white)}
.call{position:absolute;left:950px;top:30px}
.call-label{position:absolute;left:49px;top:0;font-size:19px;color:#888;white-space:nowrap}
.call-num{position:absolute;left:49px;top:30px;font-size:21px;color:var(--muted);white-space:nowrap}

/* hero */
.hero{position:absolute;left:0;top:125px;width:1200px;height:574px;overflow:hidden}
.hero-photo{position:absolute;inset:0;background:linear-gradient(90deg,#6d6a66 0%,#4d4a48 30%,#3b3a40 45%,#3a3a86 60%,#3d3c96 100%)}
.hero-title{position:absolute;left:613px;top:150px;font-family:"Montserrat",sans-serif;font-weight:500;font-size:57px;color:var(--white);letter-spacing:1px}
.hero-sub{position:absolute;left:613px;top:215px;font-size:29px;color:var(--white)}
.hero-text{position:absolute;left:613px;top:262px;width:490px;font-size:15px;line-height:25px;color:#e6e6f2}

/* about */
.about-title{position:absolute;left:78px;top:756px;font-size:36px}
.about-text{position:absolute;left:78px;top:818px;width:680px;font-size:14.5px;line-height:26px;color:var(--muted)}
.video{position:absolute;left:811px;top:762px;width:308px;height:308px;border-radius:50%;border:5px solid var(--ring);overflow:hidden}
.video-photo{position:absolute;inset:0;background:radial-gradient(circle at 55% 45%,#5c7fa4,#2b3f5c 70%)}

/* goal */
.goal{position:absolute;left:0;top:1148px;width:1200px;height:678px}
.goal-left{position:absolute;left:0;top:0;width:657px;height:678px;background:var(--dark)}
.goal-photo{position:absolute;left:657px;top:0;width:543px;height:678px;background:linear-gradient(135deg,#5e94b8 0%,#2c6389 45%,#123a5c 100%)}
.goal-title{position:absolute;left:78px;top:56px;font-family:"Montserrat",sans-serif;font-size:36px;color:var(--white);letter-spacing:1px}
.goal-card{position:absolute;left:78px;width:519px;height:112px;background:var(--white)}
.goal-card svg{position:absolute;left:20px;top:20px}
.goal-card h3{position:absolute;left:81px;top:18px;font-family:"Montserrat",sans-serif;font-weight:500;font-size:20px;line-height:26px;color:var(--indigo)}
.goal-card p{position:absolute;left:81px;top:48px;width:400px;font-size:13.5px;line-height:21px;color:var(--muted)}
.goal-card.two-line p{top:74px}

/* portfolio */
.portfolio-title{position:absolute;left:0;top:1895px;width:1200px;text-align:center;font-size:36px}
.tile{position:absolute;top:1967px;width:251px;height:313px;overflow:hidden}
.tile-photo{position:absolute;inset:0}
.tile-mark{position:absolute;left:81px;top:102px;width:90px;height:90px;border-radius:50%;background:var(--white);display:flex;align-items:center;justify-content:center;font-size:16px;font-weight:700;color:var(--ink)}
.tile-overlay{position:absolute;left:5px;top:151px;width:241px;height:152px;background:rgba(47,49,147,.85);color:var(--white);text-align:center}
.tile-overlay h4{margin-top:56px;font-weight:400;font-size:18px}
.tile-overlay p{margin:10px auto 0;width:200px;font-size:13.5px;line-height:22px}

/* blog */
.blog{position:absolute;left:0;top:2361px;width:1200px;height:723px;background:var(--light)}
.blog-title{position:absolute;left:0;top:62px;width:1200px;text-align:center;font-size:36px}
.post{position:absolute;top:198px;width:321px;height:436px}
.post-photo{height:188px}
.post-body{height:248px;background:var(--indigo);color:var(--white);padding:28px 20px 0 20px}
.post-body h3{font-size:20px;line-height:28px;font-weight:700}
.post-body p{margin-top:14px;font-size:13.5px;line-height:22px;color:#e4e4f4}
.read-more{position:absolute;left:20px;top:404px;font-size:16px;display:flex;align-items:center;gap:10px;color:var(--white)}

/* contact */
.contact{position:absolute;left:0;top:3084px;width:1200px;height:407px;background:linear-gradient(160deg,#0b5a91 0%,#0a4a7d 50%,#0c3f6b 100%)}
.contact-title{position:absolute;left:0;top:52px;width:1200px;text-align:center;font-family:"Montserrat",sans-serif;font-size:40px;color:var(--white);letter-spacing:1px}
.field{position:absolute;border:1px solid rgba(255,255,255,.75);color:var(--white);font-size:14px;padding:8px 12px}

/* footer */
.footer{position:absolute;left:0;top:3491px;width:1200px;height:422px;background:linear-gradient(160deg,#23282d,#1a1e22);border-top:5px solid var(--indigo)}
.foot-h{position:absolute;top:60px;font-family:"Montserrat",sans-serif;font-size:22px;color:var(--white);letter-spacing:1px}
.foot-text{font-size:14px;line-height:23px;color:#d8d8d8}
.foot-link{position:absolute;left:444px;font-size:15px;color:#d8d8d8}
.info{position:absolute;left:650px;display:flex;gap:14px;font-size:14.5px;line-height:22px;color:#d8d8d8}
.social{position:absolute;left:960px;display:flex;align-items:center;gap:16px;font-size:15px;color:#d8d8d8}
.social span.dot{width:34px;height:34px;border-radius:50%;border:2px solid #d8d8d8;display:block}
.foot-rule{position:absolute;left:0;top:334px;width:1200px;height:1px;background:#4a4f55}
.copyright{position:absolute;left:0;top:372px;width:1200px;text-align:center;font-size:14px;color:#cfcfcf}
</style>
</head>
<body>

<header class="site-header">
  <div class="brand">K7</div>
  <nav>
    <div class="nav-item nav-active">Home</div>
    <div class="nav-item" style="left:545px">About</div>
    <div class="nav-item" style="left:639px">Portfolio</div>
    <div class="nav-item" style="left:762px">Contact</div>
    <svg class="abs" style="left:860px;top:52px" width="24" height="24" viewBox="0 0 24 24"><circle cx="10" cy="10" r="7" fill="none" stroke="#2f3193" stroke-width="2.4"/><line x1="15" y1="15" x2="22" y2="22" stroke="#2f3193" stroke-width="2.6"/></svg>
  </nav>
  <div class="call">
    <svg width="40" height="40" viewBox="0 0 40 40"><circle cx="20" cy="20" r="20" fill="#2a4f7e"/><path d="M13 11c2-1 3 0 4 2l1 3c0 1-1 2-2 3 1 2 3 4 5 5 1-1 2-2 3-2l3 1c2 1 3 2 2 4-1 2-3 3-5 3-7-1-13-7-14-14 0-2 1-4 3-5z" fill="#fff"/></svg>
    <div class="call-label">Call us now</div>
    <div class="call-num">123-456-0789</div>
  </div>
</header>

<section class="hero">
  <div class="hero-photo" role="img" aria-label="Businesswoman holding a glowing tablet against a concrete wall, fading into an indigo panel"></div>
  <h1 class="hero-title">K7 SOFTWARE</h1>
  <p class="hero-sub">The open source software industry</p>
  <p class="hero-text">Lorem Ipsum is simply dummy text of the printing and typesetting industry. Lorem Ipsum has been the industry's standard dummy text ever since the 1500s, when an unknown printer took a galley.</p>
  <div class="btn btn-solid" style="left:514px;top:352px;width:185px;height:60px;background:#2b2d8a">Learn more</div>
  <div class="btn btn-white" style="left:712px;top:352px;width:186px;height:60px">Join now</div>
</section>

<section>
  <h2 class="heading about-title">ABOUT K7 SOFTWARE</h2>
  <p class="about-text">Lorem Ipsum is simply dummy text of the printing and typesetting industry. Lorem Ipsum has been the industry's standard dummy text ever since the 1500s, when an unknown printer took a galley of type and scrambled it to make a type specimen book. It has survived not only five centuries, but also the leap into electronic typesetting, remaining essentially unchanged. It was popularised in the 1960s with the release of Letterset sheets containing Lorem Ipsum passages, and more recently with desktop publishing software like Alden PageForge including versions of Lorem Ipsum.</p>
  <div class="btn btn-solid" style="left:78px;top:1015px;width:186px;height:58px">Learn more</div>
  <div class="video">
    <div class="video-photo" role="img" aria-label="Person working in front of large digital screens"></div>
    <svg class="abs" style="left:123px;top:123px" width="52" height="52" viewBox="0 0 52 52"><circle cx="26" cy="26" r="24" fill="none" stroke="#fff" stroke-width="3"/><path d="M20 15 L37 26 L20 37 Z" fill="#fff"/></svg>
  </div>
</section>

<section class="goal">
  <div class="goal-left"></div>
  <div class="goal-photo" role="img" aria-label="Businessman touching a glowing holographic interface"></div>
  <h2 class="goal-title">OUR GOAL</h2>

  <div class="goal-card" style="top:125px">
    <svg width="46" height="40" viewBox="0 0 46 40"><circle cx="12" cy="10" r="6" fill="#2a4f7e"/><circle cx="34" cy="10" r="6" fill="#2a4f7e"/><path d="M2 34c0-8 5-14 10-14s10 6 10 14zM24 34c0-8 5-14 10-14s10 6 10 14z" fill="#2a4f7e"/></svg>
    <h3>Binding of customers to K7 IT Group</h3>
    <p>Lorem Ipsum is simply dummy text of the printing and typesetting industry. Lorem Ipsum has industry's.</p>
  </div>
  <div class="goal-card" style="top:261px">
    <h3>Sales of subscriptions to customer</h3>
    <p>Lorem Ipsum is simply dummy text of the printing and typesetting industry. Lorem Ipsum has industry's.</p>
  </div>
  <div class="goal-card" style="top:397px">
    <svg width="40" height="42" viewBox="0 0 40 42"><circle cx="20" cy="8" r="6" fill="#2a4f7e"/><circle cx="6" cy="30" r="5" fill="#2a4f7e"/><circle cx="34" cy="30" r="5" fill="#2a4f7e"/><path d="M20 14v10M20 24L8 28M20 24l12 4" stroke="#2a4f7e" stroke-width="3" fill="none"/></svg>
    <h3>Enlarge network K7 IT Group</h3>
    <p>Lorem Ipsum is simply dummy text of the printing and typesetting industry. Lorem Ipsum has industry's.</p>
  </div>
  <div class="goal-card two-line" style="top:532px">
    <svg width="44" height="38" viewBox="0 0 44 38"><rect x="2" y="4" width="30" height="22" fill="none" stroke="#2a4f7e" stroke-width="3"/><rect x="8" y="14" width="5" height="9" fill="#2a4f7e"/><rect x="16" y="10" width="5" height="13" fill="#2a4f7e"/><circle cx="37" cy="14" r="5" fill="#2a4f7e"/><path d="M30 36c0-7 3-12 7-12s7 5 7 12z" fill="#2a4f7e"/></svg>
    <h3>USP : Sales of complete package,<br>Software, consultancy and training</h3>
    <p>Lorem Ipsum is simply dummy text of the printing.</p>
  </div>
</section>

<section>
  <h2 class="heading portfolio-title">K7 SOFTWARE PORTFOLIO</h2>
  <div class="tile" style="left:78px">
    <div class="tile-photo" role="img" aria-label="Hand holding a tablet" style="background:linear-gradient(160deg,#cfc6b8,#8d8579)"></div>
    <div class="tile-overlay"><h4>BLUE FOX</h4><p>Lorem Ipsum is simply dummy printing and typesetting</p></div>
    <div class="tile-mark" style="top:62px">Bluefox</div>
  </div>
  <div class="tile" style="left:344px">
    <div class="tile-photo" role="img" aria-label="Hands using a smartphone" style="background:linear-gradient(160deg,#6d5f5a,#2e2a2c)"></div>
    <div class="tile-mark">Crater</div>
  </div>
  <div class="tile" style="left:608px">
    <div class="tile-photo" role="img" aria-label="Team working around a table" style="background:linear-gradient(160deg,#6b5a4c,#2f2823)"></div>
    <div class="tile-mark">Velmor</div>
  </div>
  <div class="tile" style="left:874px">
    <div class="tile-photo" role="img" aria-label="Two people working on a laptop" style="background:linear-gradient(160deg,#8e8a80,#4b4a45)"></div>
    <div class="tile-mark" style="font-size:12px">Ourtrustwall</div>
  </div>
</section>

<section class="blog">
  <h2 class="heading blog-title">RECENT BLOG</h2>
  <article class="post" style="left:78px">
    <div class="post-photo" role="img" aria-label="Cheering man at a laptop" style="background:linear-gradient(160deg,#e7e2d8,#a89e8e)"></div>
    <div class="post-body"><h3>Lorem ipsum is simply dummy typesetting industry.</h3><p>Lorem Ipsum is simply dummy text of the printing and typesetting industry. Lorem Ipsum has been the industry's standard</p></div>
    <div class="read-more">READ MORE <svg width="34" height="10" viewBox="0 0 34 10"><path d="M0 5h30M26 1l5 4-5 4" stroke="#fff" stroke-width="2" fill="none"/></svg></div>
  </article>
  <article class="post" style="left:438px">
    <div class="post-photo" role="img" aria-label="Person beneath hanging light bulbs, one glowing" style="background:linear-gradient(160deg,#5a5a58,#2f2f2e)"></div>
    <div class="post-body"><h3>Lorem ipsum is simply dummy typesetting industry.</h3><p>Lorem Ipsum is simply dummy text of the printing and typesetting industry. Lorem Ipsum has been the industry's standard</p></div>
    <div class="read-more">READ MORE <svg width="34" height="10" viewBox="0 0 34 10"><path d="M0 5h30M26 1l5 4-5 4" stroke="#fff" stroke-width="2" fill="none"/></svg></div>
  </article>
  <article class="post" style="left:801px">
    <div class="post-photo" role="img" aria-label="Digital devices floating above a tablet" style="background:linear-gradient(160deg,#2d5f8a,#0f2a44)"></div>
    <div class="post-body"><h3>Lorem ipsum is simply dummy typesetting industry.</h3><p>Lorem Ipsum is simply dummy text of the printing and typesetting industry. Lorem Ipsum has been the industry's standard</p></div>
    <div class="read-more">READ MORE <svg width="34" height="10" viewBox="0 0 34 10"><path d="M0 5h30M26 1l5 4-5 4" stroke="#fff" stroke-width="2" fill="none"/></svg></div>
  </article>
</section>

<section class="contact">
  <h2 class="contact-title">CONTACT US</h2>
  <div class="field" style="left:232px;top:138px;width:313px;height:42px">Name:</div>
  <div class="field" style="left:232px;top:185px;width:313px;height:39px">Phone:</div>
  <div class="field" style="left:232px;top:229px;width:313px;height:39px">E-Mail:</div>
  <div class="field" style="left:550px;top:138px;width:415px;height:130px">Message:</div>
  <div class="btn btn-solid" style="left:527px;top:297px;width:146px;height:47px;font-size:17px">Submit</div>
</section>

<footer class="footer">
  <h3 class="foot-h" style="left:78px">ABOUT US</h3>
  <div class="abs" style="left:78px;top:102px;width:105px;height:105px;border-radius:50%;background:#f1f1f4;display:flex;align-items:center;justify-content:center;font-weight:700;font-size:28px;color:var(--indigo)">K7</div>
  <p class="foot-text abs" style="left:201px;top:96px;width:170px">Lorem Ipsum is simply dummy text of the text printing and typesetting industry. Lorem Ipsum has been the industry's</p>
  <p class="foot-text abs" style="left:78px;top:234px;width:300px">standard dummy text of the printing and typesetting industry.</p>

  <h3 class="foot-h" style="left:444px">USEFUL LINK</h3>
  <div class="foot-link" style="top:112px">Home</div>
  <div class="foot-link" style="top:157px">About</div>
  <div class="foot-link" style="top:204px">Portfolio</div>
  <div class="foot-link" style="top:248px">Contact</div>

  <h3 class="foot-h" style="left:650px">CONTACT INFO</h3>
  <div class="info" style="top:104px"><svg width="16" height="22" viewBox="0 0 16 22"><path d="M8 0a8 8 0 0 1 8 8c0 6-8 14-8 14S0 14 0 8a8 8 0 0 1 8-8z" fill="#fff"/><circle cx="8" cy="8" r="3" fill="#23282d"/></svg><span>123 Building Name, Street,<br>City, Country - Zip code</span></div>
  <div class="info" style="top:170px"><svg width="18" height="18" viewBox="0 0 18 18"><path d="M3 1c2-1 3 0 4 2l1 2c0 1-1 2-2 2 1 2 3 4 5 5 0-1 1-2 2-2l2 1c2 1 2 2 1 4-1 2-3 2-5 2C6 16 2 12 1 6c0-2 1-4 2-5z" fill="#fff"/></svg><span>123-456-0789</span></div>
  <div class="info" style="top:212px"><svg width="18" height="14" viewBox="0 0 18 14"><rect width="18" height="14" fill="#fff"/><path d="M0 0l9 8 9-8" stroke="#23282d" stroke-width="1.6" fill="none"/></svg><span>support@k7software.com</span></div>

  <h3 class="foot-h" style="left:960px">FOLLOW US ON</h3>
  <div class="social" style="top:100px"><span class="dot"></span>Facenet</div>
  <div class="social" style="top:142px"><span class="dot"></span>Chirper</div>
  <div class="social" style="top:184px"><span class="dot"></span>Linkpro</div>
  <div class="social" style="top:226px"><span class="dot"></span>Searchly</div>

  <div class="foot-rule"></div>
  <p class="copyright">Copyright © K7 SOFTWARE - 2017 &nbsp;All Rights Reserved.</p>
</footer>

</body>
</html>
```